Business card for a doctor's practice

Would like a business card for a Pulmonary ( lung) doctor. I would like to include a logo with something in reference to air or oxygen or lungs. Would like the color red included somehow. Name of the company is Breathwell Medical Associates of Eastern Ridgeford and we specialize in Pulmonary Medicine,. I would like something streamlined and modern
Target Market(s)
Patients, hospitals, other doctors
Industry/Entity Type
Business
Contact Information for Business Card
Would like business details superimposed on a logo somehow

```html
<!DOCTYPE html>
<html lang="en">
<head>
<meta charset="utf-8">
<title>Breathwell Medical Associates – Business Card</title>
<link href="https://fonts.googleapis.com/css2?family=Open+Sans:wght@400;500;700&display=swap" rel="stylesheet">
<style>
  :root {
    --brand-red: #e02128;
    --ink-grey: #555555;
    --paper: #ffffff;
    --backdrop: #eeeef0;
  }
  * { box-sizing: border-box; margin: 0; padding: 0; }
  html, body {
    width: 994px; height: 1200px; overflow: hidden;
    background: var(--backdrop);
    font-family: "Open Sans", sans-serif;
  }
  .sheet { position: relative; width: 994px; height: 1200px; }

  .brand-hero {
    position: absolute; left: 0; top: 0; width: 994px; height: 370px;
    background: var(--paper);
    display: flex; flex-direction: column; align-items: center;
    padding-top: 66px;
  }
  .brand-mark {
    width: 138px; height: 138px; border-radius: 50%;
    border: 3px solid var(--brand-red);
  }
  .wordmark {
    margin-top: 14px; text-align: center;
    color: var(--brand-red); font-weight: 500; line-height: 1.05;
  }
  .brand-hero .wordmark-main { font-size: 40px; letter-spacing: 0.5px; display: block; }
  .brand-hero .wordmark-sub { font-size: 26px; letter-spacing: 4px; display: block; margin-top: 4px; }

  .card {
    position: absolute; left: 219px; width: 552px; height: 330px;
    background: var(--paper); border-radius: 20px; overflow: hidden;
  }
  .card--first { top: 431px; }
  .card--second { top: 811px; }

  .card-logo {
    position: absolute; top: 27px; left: 0; width: 100%;
    display: flex; flex-direction: column; align-items: center;
  }
  .card-logo .brand-mark { width: 84px; height: 84px; border-width: 2px; }
  .card-logo .wordmark { margin-top: 8px; }
  .card-logo .wordmark-main { font-size: 23px; display: block; }
  .card-logo .wordmark-sub { font-size: 15px; letter-spacing: 2.5px; display: block; margin-top: 2px; }

  .info-band {
    position: absolute; left: 0; top: 194px; width: 100%; height: 109px;
    background: var(--brand-red); color: var(--paper);
  }
  .holder {
    position: absolute; right: 295px; top: 16px; text-align: right;
  }
  .holder-name { font-size: 15px; font-weight: 700; letter-spacing: 0.2px; }
  .holder-role { font-size: 13px; margin-top: 1px; }
  .holder-address { font-size: 12.5px; line-height: 17px; margin-top: 10px; }

  .contact-list {
    position: absolute; left: 280px; top: 18px; list-style: none;
    font-size: 13px; line-height: 20px;
  }
  .contact-list li { display: flex; align-items: center; gap: 6px; }
  .contact-list svg { width: 12px; height: 12px; flex: none; }
</style>
</head>
<body>
<div class="sheet">

  <section class="brand-hero">
    <div class="brand-mark"></div>
    <div class="wordmark">
      <span class="wordmark-main">BREATHWELL MEDICAL</span>
      <span class="wordmark-sub">ASSOCIATES</span>
    </div>
  </section>

  <article class="card card--first">
    <div class="card-logo">
      <div class="brand-mark"></div>
      <div class="wordmark">
        <span class="wordmark-main">BREATHWELL MEDICAL</span>
        <span class="wordmark-sub">ASSOCIATES</span>
      </div>
    </div>
    <div class="info-band">
      <div class="holder">
        <p class="holder-name">DANIEL HARROW</p>
        <p class="holder-role">President</p>
        <p class="holder-address">418 Linden Park Road,<br>Ridgeford, VA 22190</p>
      </div>
      <ul class="contact-list">
        <li><svg viewBox="0 0 12 12"><rect x="3" y="0.5" width="6" height="11" rx="1" fill="none" stroke="#fff"/><line x1="4.5" y1="9" x2="7.5" y2="9" stroke="#fff"/></svg>+ 000 000 000</li>
        <li><svg viewBox="0 0 12 12"><path d="M1 5 Q6 1 11 5 L9.5 6.5 L8 5 L4 5 L2.5 6.5 Z" fill="#fff"/><rect x="2.5" y="6" width="7" height="4.5" rx="1" fill="#fff"/></svg>+ 000 000 000</li>
        <li><svg viewBox="0 0 12 12"><rect x="0.5" y="2.5" width="11" height="7" fill="none" stroke="#fff"/><path d="M0.5 2.5 L6 7 L11.5 2.5" fill="none" stroke="#fff"/></svg>info@breathwellmed.com</li>
        <li><svg viewBox="0 0 12 12"><circle cx="6" cy="6" r="5" fill="none" stroke="#fff"/><ellipse cx="6" cy="6" rx="2.2" ry="5" fill="none" stroke="#fff"/><line x1="1" y1="6" x2="11" y2="6" stroke="#fff"/></svg>www.breathwellmed.com</li>
      </ul>
    </div>
  </article>

  <article class="card card--second">
    <div class="card-logo">
      <div class="brand-mark"></div>
      <div class="wordmark">
        <span class="wordmark-main">BREATHWELL MEDICAL</span>
        <span class="wordmark-sub">ASSOCIATES</span>
      </div>
    </div>
    <div class="info-band">
      <div class="holder">
        <p class="holder-name">DANIEL HARROW</p>
        <p class="holder-role">President</p>
        <p class="holder-address">418 Linden Park Road,<br>Ridgeford, VA 22190</p>
      </div>
      <ul class="contact-list">
        <li><svg viewBox="0 0 12 12"><rect x="3" y="0.5" width="6" height="11" rx="1" fill="none" stroke="#fff"/><line x1="4.5" y1="9" x2="7.5" y2="9" stroke="#fff"/></svg>+ 000 000 000</li>
        <li><svg viewBox="0 0 12 12"><path d="M1 5 Q6 1 11 5 L9.5 6.5 L8 5 L4 5 L2.5 6.5 Z" fill="#fff"/><rect x="2.5" y="6" width="7" height="4.5" rx="1" fill="#fff"/></svg>+ 000 000 000</li>
        <li><svg viewBox="0 0 12 12"><rect x="0.5" y="2.5" width="11" height="7" fill="none" stroke="#fff"/><path d="M0.5 2.5 L6 7 L11.5 2.5" fill="none" stroke="#fff"/></svg>info@breathwellmed.com</li>
        <li><svg viewBox="0 0 12 12"><circle cx="6" cy="6" r="5" fill="none" stroke="#fff"/><ellipse cx="6" cy="6" rx="2.2" ry="5" fill="none" stroke="#fff"/><line x1="1" y1="6" x2="11" y2="6" stroke="#fff"/></svg>www.breathwellmed.com</li>
      </ul>
    </div>
  </article>

</div>
</body>
</html>
```